Lumo Sourdough Tortilla bag design front and back

Our tortilla bags are flat plastic bags. I would like a design for the front and back of our tortillas. Our tortillas are made of whole wheat flour. We have decided to go with the following font and color scheme for our tortilla bags from the updated attached samples below. Wheat or taco images are okay to brighten and make the package stand out. We prefer a clean look. We prefer the word "Artisian" to remain in cursive.

Target Market(s)

Health conscious consumers

Industry/Entity Type

Bakery

Font styles to use
Serif
Sans Serif
Decorative

Colors
59FF00
82FF00
B8FF75
E3FFCB
F4FFEA
EB3D1F
EC4F4E
F09395
F8D3D4
FCEDEE

Requirements
Must have
• The word "sourdough must standout and be prominent on the front,
Nice to have
• Looking for clean upscale look that pops

```html
<!DOCTYPE html>
<html lang="en">
<head>
<meta charset="utf-8">
<title>Lumo Sourdough Tortilla – Front Panel</title>
<link rel="stylesheet" href="https://fonts.googleapis.com/css2?family=Archivo+Black&family=Bebas+Neue&family=Lobster&family=Montserrat:wght@800&family=Oswald:wght@400;500&family=Yellowtail&display=swap">
<style>
  :root {
    --lime: #a2d23f;
    --forest: #2b3a1f;
    --ink: #0c0d11;
    --paper: #ffffff;
  }
  html, body { margin: 0; padding: 0; overflow: hidden; background: var(--paper); }
  .package { display: block; width: 1200px; height: 1200px; }
  .brand-name { font-family: "Montserrat", sans-serif; font-weight: 800; fill: var(--forest); }
  .flavor-title { font-family: "Bebas Neue", sans-serif; fill: var(--lime); }
  .script-word { font-family: "Lobster", "Yellowtail", cursive; font-style: normal; fill: var(--paper); stroke: var(--forest); stroke-width: 7; stroke-linejoin: round; paint-order: stroke; }
  .product-type { font-family: "Archivo Black", sans-serif; fill: var(--forest); }
  .count-label { font-family: "Oswald", sans-serif; font-weight: 500; fill: var(--paper); }
  .weight-label { font-family: "Oswald", sans-serif; font-weight: 400; fill: var(--paper); }
  .storage-label { font-family: "Oswald", sans-serif; font-weight: 400; fill: var(--forest); }
</style>
</head>
<body>
<svg class="package" viewBox="0 0 1200 1200" xmlns="http://www.w3.org/2000/svg">
  <!-- bands -->
  <rect class="band-top" x="0" y="0" width="1200" height="276" fill="var(--lime)"/>
  <rect class="band-flavor" x="0" y="402" width="1200" height="331" fill="var(--ink)"/>
  <rect class="band-bottom" x="0" y="867" width="1200" height="333" fill="var(--lime)"/>

  <!-- brand -->
  <text class="brand-name" x="600" y="142" text-anchor="middle" font-size="74">LUMO</text>

  <!-- flavor -->
  <text class="flavor-title" x="290" y="618" font-size="212" textLength="617" lengthAdjust="spacingAndGlyphs">SOURDOUGH</text>
  <line class="flavor-rule" x1="289" y1="664" x2="537" y2="664" stroke="var(--lime)" stroke-width="3"/>
  <line class="flavor-rule" x1="672" y1="664" x2="916" y2="664" stroke="var(--lime)" stroke-width="3"/>
  <rect class="flavor-ornament" x="560" y="629" width="86" height="60" rx="30" fill="#3a3b3e" role="img" aria-label="Leaf ornament"/>

  <!-- product name -->
  <line class="name-rule" x1="353" y1="953" x2="470" y2="953" stroke="var(--forest)" stroke-width="4"/>
  <line class="name-rule" x1="740" y1="953" x2="847" y2="953" stroke="var(--forest)" stroke-width="4"/>
  <text class="script-word" x="605" y="942" text-anchor="middle" font-size="78" textLength="262" lengthAdjust="spacingAndGlyphs">Artisan</text>
  <text class="product-type" x="356" y="1045" font-size="86" textLength="494" lengthAdjust="spacingAndGlyphs">TORTILLAS</text>

  <!-- diet badges -->
  <rect class="badge" x="73" y="960" width="169" height="66" rx="8" fill="var(--forest)" opacity="0.85"/>
  <circle class="badge" cx="90" cy="1092" r="30" fill="var(--forest)" opacity="0.85"/>
  <circle class="badge" cx="162" cy="1092" r="30" fill="var(--forest)" opacity="0.85"/>
  <circle class="badge" cx="237" cy="1092" r="30" fill="var(--forest)" opacity="0.85"/>

  <!-- count & weight -->
  <rect class="count-box" x="985" y="980" width="117" height="67" fill="var(--forest)"/>
  <text class="count-label" x="1043" y="1036" text-anchor="middle" font-size="54">8CT</text>
  <text class="weight-label" x="985" y="1080" font-size="24">NET WEIGHT</text>
  <line x1="1092" y1="1079" x2="1150" y2="1079" stroke="var(--paper)" stroke-width="2"/>
  <text class="weight-label" x="985" y="1108" font-size="24">12 OUNCES / 243 G</text>

  <!-- storage -->
  <rect class="storage-box" x="524" y="1118" width="144" height="34" rx="3" fill="none" stroke="var(--forest)" stroke-width="2"/>
  <text class="storage-label" x="596" y="1145" text-anchor="middle" font-size="24">KEEP FROZEN</text>
  <g class="snowflake" stroke="var(--forest)" stroke-width="3" stroke-linecap="round" transform="translate(680 1126)">
    <line x1="0" y1="-12" x2="0" y2="12"/>
    <line x1="-10.4" y1="-6" x2="10.4" y2="6"/>
    <line x1="-10.4" y1="6" x2="10.4" y2="-6"/>
  </g>
</svg>
</body>
</html>
```